Etiketten für Imkerei aus der Steiermark
Zielgruppe
Wir sind eine Imkerei aus der Steiermark / Österreich im Vollerwerb. www.talmann-biene.at
Zielgruppe: Frauen, Familien, Regional
Unser Image: hohe Qualität, Familienbetrieb, naturnah, gesund
Vermarktung: Direkt, Verkaufsstellen, Märkte, zukünftig auch online
Aufgabenstellung
Wir werden die Honiggläser und die Druckerei umstellen und möchten hierfür ein profesionelles abgestimmtes Design. Unser Logo soll erhalten bleiben. Die Honigsortenbezeichnung (Waldhonig, Cremehonig, Blütenhonig) soll zukünftig eingedruckt werden und neben dem Logo ein Zentrales Element sein.
In Zukunft verwenden wir Vintra Gläser mit hohen Deckel der Firma Glasoria in den Größen 1000g(Lise 785), 500g (Vin 410), 250 g (Vin 212) und 150 g (Vin 125). Der Deckel soll einheitlich Gold oder Silber sein.

```html
<!DOCTYPE html>
<html lang="de">
<head>
<meta charset="utf-8">
<title>Talmann Biene – Blütenhonig Etikett</title>
<link rel="stylesheet" href="https://fonts.googleapis.com/css2?family=Barlow+Condensed:wght@300;400;600&family=Archivo+Black&family=Almendra&display=swap">
<style>
  :root {
    --label-cream: #fdfcdc;
    --comb-line: #e8e6cc;
    --ink: #000000;
    --mark-glow: #f4f39a;
  }
  html, body {
    margin: 0;
    padding: 0;
    overflow: hidden;
    background: #ffffff;
  }
  .label {
    position: relative;
    width: 1200px;
    height: 368px;
    overflow: hidden;
    background: var(--label-cream);
    color: var(--ink);
    font-family: "Barlow Condensed", sans-serif;
  }
  .comb-pattern {
    position: absolute;
    inset: 0;
    background: linear-gradient(180deg, var(--label-cream), #faf8d4);
    box-shadow: inset 0 0 0 2px var(--comb-line);
  }
  .contact {
    position: absolute;
    left: 32px;
    top: 82px;
    margin: 0;
    font-style: normal;
    font-weight: 300;
    font-size: 22px;
    line-height: 28.3px;
  }
  .contact .company {
    font-weight: 600;
    font-size: 22px;
    letter-spacing: 0.2px;
    line-height: 26px;
    margin-bottom: 1px;
  }
  .weight {
    position: absolute;
    right: 17px;
    top: 14px;
    font-size: 37px;
    font-weight: 400;
  }
  .brand {
    position: absolute;
    left: 480px;
    top: 83px;
    width: 240px;
    height: 200px;
    display: flex;
    align-items: center;
    justify-content: center;
  }
  .brand-dot {
    position: absolute;
    width: 150px;
    height: 150px;
    border-radius: 50%;
    background: var(--mark-glow);
  }
  .brand-name {
    position: relative;
    font-family: "Archivo Black", sans-serif;
    font-size: 30px;
    line-height: 1.05;
    text-align: center;
    color: var(--ink);
  }
  .tagline {
    position: absolute;
    left: 384px;
    top: 288px;
    width: 442px;
    margin: 0;
    text-align: center;
    font-family: "Almendra", serif;
    font-size: 37px;
    font-weight: 400;
    white-space: nowrap;
  }
  .variety {
    position: absolute;
    left: 804px;
    top: 143px;
    margin: 0;
    font-family: "Archivo Black", sans-serif;
    font-size: 57px;
    font-weight: 400;
    white-space: nowrap;
  }
  .storage {
    position: absolute;
    right: 19px;
    top: 263px;
    margin: 0;
    text-align: right;
    font-weight: 600;
    font-size: 24px;
    line-height: 28px;
  }
  .best-before {
    position: absolute;
    right: 19px;
    top: 327px;
    margin: 0;
    font-weight: 300;
    font-size: 22px;
    white-space: nowrap;
  }
  .best-before .date {
    font-size: 26px;
    margin-left: 12px;
  }
</style>
</head>
<body>
<main class="label">
  <div class="comb-pattern" role="img" aria-label="Honigwaben-Muster als Hintergrund"></div>

  <address class="contact">
    <div class="company">MEISTERIMKEREI TALMANN</div>
    Theresa und Markus<br>
    Birkenweg 12<br>
    8160 Almhofen<br>
    Tel: 0664 / 12 34 567<br>
    talmann-biene@mail.at<br>
    www.talmann-biene.at
  </address>

  <div class="weight">1000 g</div>

  <div class="brand">
    <span class="brand-dot"></span>
    <span class="brand-name">Talmann<br>Biene</span>
  </div>

  <p class="tagline">Österreichischer Qualitätshonig</p>

  <h1 class="variety">Blütenhonig</h1>

  <p class="storage">Trocken und vor Wärme<br>geschützt lagern!</p>

  <p class="best-before">Mindestens haltbar bis: <span class="date">03 / 10 / 2030</span></p>
</main>
</body>
</html>
```